I am a company selling interior designing materials

HI, I am selling interior design materials and require a namecard which is more outstanding while following a certain details placement as attached.

My clients are mainly interior designers so it has to attract their attention rather than feeling that its "just another namecard". I am selling wallcoverings, fabrics, acoustics and carpets.

Target Market(s)

interior designers designing hotels, commerical offices.

Contact Information for Business Card

As per attached.
Please change address to 47 Jalan 16 Tampines #05-02 Velmora Building Singapore 527314

Font styles to use
Other font styles liked:
• calibri

Requirements
Must have
• (1) company logo on top in the middle. Placement of contac details to be the same
• (2) company color is blue/green cymk 75/8/42/0
• (3) "KTV" logo to be prominent
• (4) You may change the logo but there should be a "swirl" surrounding the word KTV like current logo. The swirl pattern does not need to follow current logo and you may propose.
Should not have
• (1) there should not be any designs above "KTV" logo
• (2) no sharp triangles or angles

```html
<!DOCTYPE html>
<html lang="en">
<head>
<meta charset="utf-8">
<title>KTV Business Card</title>
<link rel="stylesheet" href="https://fonts.googleapis.com/css2?family=Open+Sans:wght@400;600;700&display=swap">
<style>
  :root {
    --brand-teal: #23a08f;
    --ink-dark: #4a4a4a;
    --ink-body: #555555;
    --card-white: #ffffff;
    --card-shade: #ececec;
    --backdrop: #464646;
  }
  * { margin: 0; padding: 0; box-sizing: border-box; }
  html, body { width: 1200px; height: 1200px; overflow: hidden; }
  body {
    background: var(--backdrop);
    font-family: "Open Sans", Calibri, Arial, sans-serif;
    display: flex;
    flex-direction: column;
    align-items: center;
    justify-content: center;
    gap: 44px;
  }
  .card {
    position: relative;
    width: 900px;
    height: 514px;
    overflow: hidden;
    background: var(--card-white);
    box-shadow: 0 14px 30px rgba(0,0,0,0.35);
  }
  .card-shape { position: absolute; inset: 0; width: 100%; height: 100%; }
  .card-content { position: absolute; inset: 0; }

  .brand-mark {
    position: absolute;
    left: 50%;
    transform: translateX(-50%);
    display: flex;
    align-items: center;
    gap: 16px;
    color: var(--ink-dark);
    font-weight: 700;
    letter-spacing: 2px;
    line-height: 1;
  }
  .brand-dot { border-radius: 50%; background: var(--brand-teal); }

  /* Front */
  .card-front .brand-mark { top: 150px; font-size: 110px; }
  .card-front .brand-dot { width: 30px; height: 30px; }
  .service-list {
    position: absolute;
    top: 345px;
    left: 0; right: 0;
    display: flex;
    justify-content: center;
    gap: 34px;
    list-style: none;
    font-size: 19px;
    font-weight: 700;
    color: var(--ink-dark);
  }
  .service-list li::before {
    content: "";
    display: inline-block;
    width: 7px; height: 7px;
    margin: 0 7px 3px 0;
    border-radius: 50%;
    background: var(--brand-teal);
  }

  /* Back */
  .card-back .brand-mark { top: 44px; font-size: 56px; gap: 10px; }
  .card-back .brand-dot { width: 16px; height: 16px; }
  .company-name {
    position: absolute;
    top: 116px; left: 0; right: 0;
    text-align: center;
    font-size: 15px;
    font-weight: 700;
    color: var(--ink-dark);
  }
  .person-name {
    position: absolute;
    top: 156px; left: 0; right: 0;
    text-align: center;
    font-size: 48px;
    color: var(--brand-teal);
    font-weight: 400;
    line-height: 1.1;
  }
  .person-name .first { font-weight: 700; }
  .mobile {
    position: absolute;
    top: 218px; left: 0; right: 0;
    text-align: center;
    font-size: 24px;
    color: var(--ink-body);
  }
  .divider {
    position: absolute;
    top: 268px; left: 230px;
    width: 440px; height: 2px;
    background: linear-gradient(90deg, transparent, #cfcfcf, transparent);
  }
  .contact-line {
    position: absolute;
    display: flex;
    align-items: center;
    gap: 10px;
    font-size: 19px;
    color: var(--ink-body);
    line-height: 1.3;
  }
  .icon { flex: 0 0 auto; width: 28px; height: 28px; }
  .address { left: 140px; top: 390px; align-items: flex-start; }
  .address .icon { margin-top: 2px; }
  .office-phone { left: 560px; top: 312px; }
  .email { left: 560px; top: 350px; }
</style>
</head>
<body>

<section class="card card-front" aria-label="Card front">
  <svg class="card-shape" viewBox="0 0 900 514" preserveAspectRatio="none" aria-hidden="true">
    <defs>
      <radialGradient id="frontSheen" cx="0.5" cy="0.4" r="0.7">
        <stop offset="0" stop-color="#ffffff"/>
        <stop offset="1" stop-color="#e6e6e6"/>
      </radialGradient>
    </defs>
    <rect width="900" height="514" fill="var(--brand-teal)"/>
    <path d="M150 0 H900 V250 C880 390 830 470 770 514 H0 V400 C10 220 60 80 150 0 Z" fill="url(#frontSheen)"/>
  </svg>
  <div class="card-content">
    <div class="brand-mark"><span class="brand-dot"></span><span>KTV</span></div>
    <ul class="service-list">
      <li>Wallcoverings</li>
      <li>Acoustic</li>
      <li>Fabrics</li>
      <li>Carpet</li>
    </ul>
  </div>
</section>

<section class="card card-back" aria-label="Card back">
  <svg class="card-shape" viewBox="0 0 900 514" preserveAspectRatio="none" aria-hidden="true">
    <defs>
      <radialGradient id="backSheen" cx="0.5" cy="0.45" r="0.7">
        <stop offset="0" stop-color="#ffffff"/>
        <stop offset="1" stop-color="#e6e6e6"/>
      </radialGradient>
    </defs>
    <rect width="900" height="514" fill="var(--brand-teal)"/>
    <path d="M150 0 H900 V250 C880 390 830 470 770 514 H0 V400 C10 220 60 80 150 0 Z" fill="url(#backSheen)"/>
  </svg>
  <div class="card-content">
    <div class="brand-mark"><span class="brand-dot"></span><span>KTV</span></div>
    <p class="company-name">Kestrel Textile Ventures Pte Ltd</p>
    <h1 class="person-name"><span class="first">Serena</span> Tan</h1>
    <p class="mobile">(65) 9172 4605</p>
    <div class="divider"></div>

    <p class="contact-line address">
      <svg class="icon" viewBox="0 0 28 28" aria-hidden="true">
        <circle cx="14" cy="14" r="12.5" fill="none" stroke="var(--brand-teal)" stroke-width="2"/>
        <path d="M7 14.5 L14 8 L21 14.5 M9.5 13 V20 H18.5 V13" fill="none" stroke="var(--brand-teal)" stroke-width="2" stroke-linejoin="round"/>
      </svg>
      <span>47 Jalan 16 Tampines #05-02<br>Velmora Building Singapore 527314</span>
    </p>
    <p class="contact-line office-phone">
      <svg class="icon" viewBox="0 0 28 28" aria-hidden="true">
        <circle cx="14" cy="14" r="12.5" fill="none" stroke="var(--brand-teal)" stroke-width="2"/>
        <path d="M9 8 C8 12 12 19 19 20 L20.5 17.5 L17.5 15.5 L16 17 C14 16 12 14 11 12 L12.5 10.5 L10.5 7.5 Z" fill="var(--brand-teal)"/>
      </svg>
      <span>(65) 6213 7840</span>
    </p>
    <p class="contact-line email">
      <svg class="icon" viewBox="0 0 28 28" aria-hidden="true">
        <circle cx="14" cy="14" r="12.5" fill="none" stroke="var(--brand-teal)" stroke-width="2"/>
        <rect x="7.5" y="9.5" width="13" height="9" rx="1" fill="var(--brand-teal)"/>
        <path d="M8 10 L14 15 L20 10" fill="none" stroke="#ffffff" stroke-width="1.4"/>
      </svg>
      <span>serena@ktvinteriors.com</span>
    </p>
  </div>
</section>

</body>
</html>
```